Business Card & Logo Design - Hedge Fund

We need a business card and logo design for a hedge fund. The hedge fund is named Morvane Holdings LLC. Morvane Holdings was created by finance professors and the strategy is based academic research that looks for patterns in stock prices. The design should look conservative, solid, strong. We favor a classic style - nothing flashy. The logo can relate to the name Morvane Holdings, or it could involve a symbol design that connotes "science" . We are open to ideas. We do not want alot of colors - but if any, color - blue is preferred. The font that seems to look best for the name (Morvane Holdings) is arial black. We are open to ideas. Most important - we want to see a mock up of an actual business card with the logo concept embedded. The business card should include space for : company name, individual name, position title, cell phone, address. We hope to have this work done by Sept. 8.

Target Market(s)

We will be meeting with and giving the business card to institutions and high net worth individuals.

Industry/Entity Type

Investment Advisory

Contact Information for Business Card

Company name - Morvane Holdings LLC
Individual name - Peter Vosk
Title - Portfolio Manager
Cell - (482) 555-0137
Address - 2750 Birchwell Lane, Suite 300, Atlanta GA 30327

Font styles to use
Other font styles liked:
• Arial

Colors
3277b5
0255a3
85acd3
cedeed
fdf9cf
d9d9d9
e6e6e6
f04a50
6b449b

Requirements
Must have
• Must have card details that are sited above.
• We would like a logo related to the name (Morvane Holdings) or concept of the fund.
Nice to have
• We want conservative / understated / clean crisp look.
• If any colors - we prefer conservative appearance - blue / gray.
• I have enclosed an example of a card style that looks attractive - please do not exactly copy this card. This is not our company or logo. I feel the layout is attractive - just as an example
Should not have
• Avoid too much color.
• I have selected some preferred colors. Please do not use all of the colors - I have selected a few that might work - but I am not sure. We are open to your ideas so please do not feel the need to use all or any of these.

```html
<!DOCTYPE html>
<html lang="en">
<head>
<meta charset="UTF-8">
<title>Morvane Holdings LLC – Business Card</title>
<link href="https://fonts.googleapis.com/css2?family=Archivo+Black&family=Lato:wght@400;700&display=swap" rel="stylesheet">
<style>
  :root {
    --stage: #3a3a38;
    --card-dark: #141414;
    --card-light: #ffffff;
    --ink: #111111;
    --blue: #0255a3;
    --blue-bright: #3277b5;
    --white: #ffffff;
  }
  * { box-sizing: border-box; margin: 0; padding: 0; }
  html, body {
    width: 1200px; height: 824px; overflow: hidden;
    background: var(--stage);
    font-family: "Lato", Arial, sans-serif;
  }
  .stage {
    width: 1200px; height: 824px;
    display: flex; align-items: center; justify-content: center; gap: 40px;
  }
  .card {
    width: 540px; height: 309px;
    position: relative;
    box-shadow: 0 10px 30px rgba(0,0,0,.45);
  }
  /* back of card */
  .card--back {
    background: var(--card-dark);
    display: flex; flex-direction: column; align-items: center; justify-content: center;
  }
  .wordmark {
    display: flex; align-items: center; gap: 14px;
  }
  .wordmark__square { width: 22px; height: 22px; }
  .wordmark__name {
    font-family: "Archivo Black", "Arial Black", sans-serif;
    line-height: 1.05; letter-spacing: .5px; text-transform: uppercase;
  }
  .card--back .wordmark__square { background: var(--blue-bright); }
  .card--back .wordmark__name { color: var(--white); font-size: 30px; }
  .website {
    margin-top: 26px;
    color: var(--blue-bright); font-size: 14px; letter-spacing: 2px; text-transform: uppercase;
  }
  /* front of card */
  .card--front {
    background: var(--card-light);
    display: flex; align-items: center;
  }
  .front__brand {
    width: 245px; display: flex; justify-content: center; padding-left: 20px;
  }
  .card--front .wordmark { gap: 10px; }
  .card--front .wordmark__square { background: var(--blue); width: 16px; height: 16px; }
  .card--front .wordmark__name { color: var(--ink); font-size: 20px; }
  .front__divider {
    width: 2px; height: 150px; background: var(--blue);
  }
  .front__details { padding-left: 24px; color: var(--ink); }
  .person__name {
    font-family: "Archivo Black", "Arial Black", sans-serif;
    font-size: 19px; text-transform: uppercase; letter-spacing: .5px;
  }
  .person__title {
    color: var(--blue); font-size: 14px; text-transform: uppercase; margin-bottom: 14px;
  }
  .contact { list-style: none; font-size: 13.5px; line-height: 1.45; }
  .contact li { display: flex; align-items: flex-start; gap: 8px; margin-bottom: 3px; }
  .contact svg { width: 12px; height: 12px; margin-top: 3px; flex: none; fill: var(--blue); }
</style>
</head>
<body>
<main class="stage">
  <section class="card card--back" aria-label="Card back">
    <div class="wordmark">
      <span class="wordmark__square"></span>
      <div class="wordmark__name">Morvane<br>Holdings LLC</div>
    </div>
    <p class="website">www.morvaneholdings.com</p>
  </section>

  <section class="card card--front" aria-label="Card front">
    <div class="front__brand">
      <div class="wordmark">
        <span class="wordmark__square"></span>
        <div class="wordmark__name">Morvane<br>Holdings LLC</div>
      </div>
    </div>
    <div class="front__divider"></div>
    <div class="front__details">
      <h1 class="person__name">Peter Vosk</h1>
      <p class="person__title">Portfolio Manager</p>
      <ul class="contact">
        <li>
          <svg viewBox="0 0 24 24" aria-hidden="true"><path d="M6.6 10.8a15.1 15.1 0 0 0 6.6 6.6l2.2-2.2c.3-.3.7-.4 1-.2 1.1.4 2.3.6 3.6.6.6 0 1 .4 1 1V20c0 .6-.4 1-1 1A17 17 0 0 1 3 4c0-.6.4-1 1-1h3.5c.6 0 1 .4 1 1 0 1.3.2 2.5.6 3.6.1.3 0 .7-.2 1z"/></svg>
          <span>(482) 555-0137</span>
        </li>
        <li>
          <svg viewBox="0 0 24 24" aria-hidden="true"><path d="M2 5h20v14H2z M2 5l10 8 10-8" /></svg>
          <span>pvosk@morvaneholdings.com</span>
        </li>
        <li>
          <svg viewBox="0 0 24 24" aria-hidden="true"><path d="M12 2a7 7 0 0 0-7 7c0 5.2 7 13 7 13s7-7.8 7-13a7 7 0 0 0-7-7zm0 9.5A2.5 2.5 0 1 1 12 6.5a2.5 2.5 0 0 1 0 5z"/></svg>
          <span>2750 Birchwell Lane,<br>Suite 300, Atlanta GA 30327</span>
        </li>
      </ul>
    </div>
  </section>
</main>
</body>
</html>
```